We have over 30 years of experience in various construction projects. New additions, rehab work, interior and exterior etc. We started our own company about a year ago.
I am attaching a card that I received from a client that I really like and would like to follow as a template, but I am very open to your creative approach. I am interested in my logo (which will be later used for my website) to incorporate the "M&P" or "M&P Remodeling" Please email me at mpremodeling 81@brindlemail.com or call Walt at 773-555-0182.

Industry/Entity Type

Construction

Contact Information for Business Card

M&P Remodeling and Beacon Services
2816 W Oakridge Ave
Brindle Heights, IL 60999
708-555-0147 - Polish
708-555-0163 - English

Piotr Walek - Owner
Marek WAlek Jr - Construction Manager
mpremodeling81@brindlemail.com

```html
<!DOCTYPE html>
<html lang="en">
<head>
<meta charset="utf-8">
<title>M&amp;P Remodeling and Beacon Services – Business Card</title>
<link rel="stylesheet" href="https://fonts.googleapis.com/css2?family=Roboto+Condensed:wght@300;400;700&display=swap">
<style>
  :root {
    --page: #e9e7e3;
    --card-black: #0b0c0e;
    --card-grey: #2a2c30;
    --card-grey-dark: #1c1d20;
    --brand-blue: #2f86d6;
    --brand-blue-light: #4fa6ee;
    --brand-blue-deep: #1a5d9c;
    --label-grey: #8b8f96;
    --ink-dark: #0c1e31;
    --text-font: "Roboto Condensed", Arial, sans-serif;
  }
  * { box-sizing: border-box; margin: 0; padding: 0; }
  html, body {
    width: 1200px; height: 1023px; overflow: hidden;
    background: var(--page);
    font-family: var(--text-font);
  }
  .card {
    position: absolute; left: 200px;
    width: 800px; height: 457px;
    border-radius: 6px; overflow: hidden;
    box-shadow: 0 10px 26px rgba(0,0,0,.28);
  }
  /* ---------- front ---------- */
  .card-front { top: 40px; background: var(--card-black); }
  .front-brand { position: absolute; left: 52px; top: 46px; }
  .brand-name {
    display: flex; align-items: center; gap: 14px;
    color: var(--brand-blue); font-weight: 700;
    font-size: 46px; line-height: 1; letter-spacing: .5px;
    white-space: nowrap;
  }
  .brand-mark { width: 22px; height: 22px; background: var(--brand-blue); flex: none; }
  .brand-sub {
    color: var(--brand-blue); font-weight: 400;
    font-size: 20px; margin: 6px 0 0 36px; letter-spacing: .5px;
  }
  .skyline-band {
    position: absolute; left: 0; top: 150px; width: 100%; height: 62px;
    background: linear-gradient(90deg, var(--brand-blue-deep), var(--brand-blue) 40%, var(--brand-blue-deep) 100%);
    opacity: .85;
  }
  .name-band {
    position: absolute; left: 0; top: 212px; width: 100%; height: 48px;
    background: linear-gradient(90deg, var(--brand-blue-light), var(--brand-blue) 55%, var(--card-grey) 100%);
  }
  .person-name {
    position: absolute; top: 0; line-height: 48px;
    color: var(--ink-dark); font-size: 26px; font-weight: 400;
    letter-spacing: 1px; text-transform: uppercase; white-space: nowrap;
  }
  .person-owner { left: 90px; }
  .person-manager { left: 302px; }
  .name-divider {
    position: absolute; left: 272px; top: 9px;
    width: 2px; height: 30px; background: var(--ink-dark); opacity: .7;
  }
  .lower-panel {
    position: absolute; left: 0; top: 260px; width: 100%; height: 197px;
    background: linear-gradient(180deg, var(--card-grey), var(--card-grey-dark));
  }
  .role {
    position: absolute; top: 8px;
    color: var(--label-grey); font-size: 15px; font-weight: 300; white-space: nowrap;
  }
  .role-owner { left: 90px; }
  .role-manager { left: 302px; }
  .contact-list {
    position: absolute; left: 90px; top: 48px; list-style: none;
    color: var(--brand-blue); font-size: 20px; line-height: 34px; white-space: nowrap;
  }
  .contact-list .lang { color: var(--brand-blue-light); }
  .phone-second { margin-left: 16px; }
  /* ---------- back ---------- */
  .card-back {
    top: 526px;
    background: linear-gradient(160deg, #3a3c41, var(--card-grey-dark));
    display: flex; flex-direction: column; align-items: center; justify-content: center;
  }
  .card-back .brand-name { font-size: 72px; gap: 20px; }
  .card-back .brand-mark { width: 34px; height: 34px; }
  .card-back .brand-sub { font-size: 32px; margin: 10px 0 0 54px; }
</style>
</head>
<body>
  <section class="card card-front">
    <div class="front-brand">
      <div class="brand-name"><span class="brand-mark"></span>M&amp;P Remodeling</div>
      <div class="brand-sub">and Beacon Services</div>
    </div>
    <div class="skyline-band" role="img" aria-label="Blue city skyline silhouette running across the card"></div>
    <div class="name-band">
      <span class="person-name person-owner">Piotr Walek</span>
      <span class="name-divider"></span>
      <span class="person-name person-manager">Marek Walek Jr</span>
    </div>
    <div class="lower-panel">
      <span class="role role-owner">Owner</span>
      <span class="role role-manager">Construction Manager</span>
      <ul class="contact-list">
        <li>708-555-0147 <span class="lang">[ Polish ]</span><span class="phone-second">708-555-0163 <span class="lang">[ English ]</span></span></li>
        <li>mpremodeling81@brindlemail.com</li>
        <li>2816 W Oakridge Ave Brindle Heights, IL 60999</li>
      </ul>
    </div>
  </section>

  <section class="card card-back">
    <div class="brand-name"><span class="brand-mark"></span>M&amp;P Remodeling</div>
    <div class="brand-sub">and Beacon Services</div>
  </section>
</body>
</html>
```